Save the date for wedding

A save the date for our wedding. We're looking for a simple and sleek invite. I would prefer not alot of calligraphy. Minimalism is good. The basic info to include is as follows:
Names: Mona and Felix
Date: June 9th
Where: Ottawa, Ontario
In small print please include that there will be a reception in Edmonton AB September 1st for those who cannot make it to Ottawa.
Please see the attached file for a style idea. Doesn’t have to be exactly like that, but something like that.

```html
<!DOCTYPE html>
<html lang="en">
<head>
<meta charset="utf-8">
<title>Save the Date – Mona and Felix</title>
<link rel="stylesheet" href="https://fonts.googleapis.com/css2?family=Montserrat:wght@500;600;700;800&family=Roboto:wght@400&display=swap">
<style>
  :root {
    --mint: #97cfc3;
    --ink: #111111;
  }
  html, body {
    margin: 0;
    padding: 0;
    width: 1200px;
    height: 857px;
    overflow: hidden;
    background: var(--mint);
  }
  .save-the-date-card {
    display: block;
    width: 1200px;
    height: 857px;
    background: var(--mint);
  }
  .arched-heading {
    font-family: "Montserrat", sans-serif;
    font-weight: 800;
    font-size: 44px;
    letter-spacing: 9px;
    fill: var(--ink);
  }
  .curved-subheading {
    font-family: "Montserrat", sans-serif;
    font-weight: 800;
    font-size: 40px;
    letter-spacing: 7px;
    fill: var(--ink);
  }
  .intro-line {
    font-family: "Montserrat", sans-serif;
    font-weight: 600;
    font-size: 30px;
    fill: var(--ink);
  }
  .couple-names {
    font-family: "Montserrat", sans-serif;
    font-weight: 800;
    font-size: 50px;
    letter-spacing: 5px;
    fill: var(--ink);
  }
  .event-date {
    font-family: "Montserrat", sans-serif;
    font-weight: 600;
    font-size: 34px;
    letter-spacing: 6px;
    fill: var(--ink);
  }
  .event-place {
    font-family: "Montserrat", sans-serif;
    font-weight: 600;
    font-size: 32px;
    letter-spacing: 1px;
    fill: var(--ink);
  }
  .reception-note {
    font-family: "Roboto", sans-serif;
    font-weight: 400;
    font-size: 21px;
    fill: var(--ink);
  }
  .rule {
    stroke: var(--ink);
    stroke-width: 4;
  }
</style>
</head>
<body>
<svg class="save-the-date-card" viewBox="0 0 1200 857" xmlns="http://www.w3.org/2000/svg">
  <defs>
    <path id="arch-top" d="M 345 192 Q 600 116 860 192" fill="none"/>
    <path id="arch-smile" d="M 378 318 Q 600 348 828 318" fill="none"/>
  </defs>

  <text class="arched-heading">
    <textPath href="#arch-top" startOffset="50%" text-anchor="middle">SAVE THE DATE</textPath>
  </text>

  <line class="rule" x1="298" y1="213" x2="902" y2="213"/>

  <text class="intro-line" x="600" y="259" text-anchor="middle">FOR THE WEDDING</text>

  <text class="curved-subheading">
    <textPath href="#arch-smile" startOffset="50%" text-anchor="middle">CELEBRATION</textPath>
  </text>

  <text class="intro-line" x="600" y="405" text-anchor="middle">OF</text>

  <text class="couple-names" x="600" y="466" text-anchor="middle">MONA AND FELIX</text>

  <line class="rule" x1="287" y1="483" x2="890" y2="483"/>

  <text class="event-date" x="600" y="530" text-anchor="middle">06.09.2018</text>
  <text class="event-place" x="600" y="572" text-anchor="middle">Ottawa, Ontario</text>

  <text class="reception-note" x="598" y="705" text-anchor="middle">There will be a reception in Edmonton AB September 1st</text>
  <text class="reception-note" x="598" y="735" text-anchor="middle">for those who cannot make it to Ottawa.</text>
</svg>
</body>
</html>
```